Conveyancing Brochure

I am after a 4 page brochure for our Conveyancing division in our law firm Drovane Pitt Hollis Lawyers.

We are a diverse range of energetic, dynamic and innovative professionals who strive to be at the forefront of progressive legal service. Please refer to our website for more information: www.dphlegal-example.com.au

I would like to see the colours of our logo & also some images incorporated throughout the brochure (however I don't want it to look 'too busy' either).

The images can be based around the range of services that we provide eg: residential, development etc.

Thank you,
Mabel

```html
<!DOCTYPE html>
<html lang="en">
<head>
<meta charset="utf-8">
<title>Drovane Pitt Hollis Lawyers – Conveyancing Brochure Spread</title>
<link rel="stylesheet" href="https://fonts.googleapis.com/css2?family=Ubuntu:wght@400;500;700&display=swap">
<style>
  :root {
    --stage: #e3e4e6;
    --teal: #1a7d9e;
    --teal-veil: rgba(26, 125, 158, 0.84);
    --photo-top: #46525e;
    --photo-bottom: #1c232b;
    --ink-light: #ffffff;
  }
  html, body {
    margin: 0;
    padding: 0;
    width: 1200px;
    height: 841px;
    overflow: hidden;
    background: var(--stage);
    font-family: "Ubuntu", sans-serif;
  }
  .spread {
    position: absolute;
    left: 80px;
    top: 52px;
    width: 1040px;
    height: 736px;
    box-shadow: 0 14px 40px rgba(0, 0, 0, 0.28);
    overflow: hidden;
  }
  .spread-photo {
    position: absolute;
    inset: 0;
    background: linear-gradient(180deg, var(--photo-top) 0%, var(--photo-bottom) 100%);
  }
  .intro-panel {
    position: absolute;
    left: 0;
    top: 0;
    width: 430px;
    height: 100%;
    box-sizing: border-box;
    padding: 46px 24px 40px 34px;
    background: var(--teal);
    color: var(--ink-light);
  }
  .intro-panel h2 {
    font-weight: 400;
    font-size: 19px;
    line-height: 1.15;
    margin: 0 0 8px;
  }
  .intro-panel p {
    font-size: 12.5px;
    line-height: 1.35;
    margin: 0 0 30px 20px;
  }
  .difference-list {
    font-size: 12.5px;
    line-height: 1.35;
    margin: 0 0 54px;
    padding-left: 40px;
  }
  .intro-panel .closing {
    margin: 0 0 16px 0;
  }
  .contact strong { font-weight: 700; }
  .services-panel {
    position: absolute;
    left: 544px;
    top: 222px;
    width: 330px;
    height: 350px;
    box-sizing: border-box;
    padding: 22px 20px 16px 24px;
    background: var(--teal-veil);
    color: var(--ink-light);
  }
  .services-panel h2 {
    font-weight: 400;
    font-size: 20px;
    margin: 0 0 8px;
  }
  .services-list {
    margin: 0;
    padding-left: 16px;
    font-size: 12px;
    line-height: 1.32;
  }
</style>
</head>
<body>
  <main class="spread">
    <div class="spread-photo" role="img" aria-label="Photograph: night city skyline through office windows with a businessman on the phone"></div>

    <section class="intro-panel">
      <h2>What is conveyancing?</h2>
      <p>Simply put, conveyancing is the legal process in transferring title between two or more parties. There are a few steps involved between signing the contract and settlement, and you will need the right people to guide you along the way. Whether you are buying or selling, our team of experienced lawyers can help.</p>

      <h2>Why use a lawyer and not a conveyancer</h2>
      <p>A lawyer and conveyancer perform the same services in a simple conveyance, but you will need a lawyer if a complex legal issue arises. We can provide you with the right advice and options to ensure that the conveyance process is as smooth as possible.</p>

      <h2>The Drovane Pitt Hollis Lawyers difference</h2>
      <ul class="difference-list">
        <li>Specialist conveyancing services from as low as $1,200</li>
        <li>Unlimited contracts review</li>
        <li>Fast response time</li>
        <li>Professional and reliable service</li>
        <li>One-stop-shop for all your legal, financial and accounting requirements for your sale and purchase</li>
      </ul>

      <p class="closing">Consider using one of our experienced lawyers and not a conveyancer to handle the legal work associated with your transaction.</p>
      <p class="closing contact">For advice on conveyancing or a quote, please contact us on <strong>1300 555 018</strong> or email <strong>enquiries@dphlegal-example.com.au</strong>.</p>
    </section>

    <section class="services-panel">
      <h2>Services</h2>
      <ul class="services-list">
        <li>Preparation of contracts</li>
        <li>Pre-contractual review of contract</li>
        <li>Advice on terms of the contract</li>
        <li>Negotiate terms with the vendor/purchaser</li>
        <li>Advise you as to various searches required and obtain searches on your behalf</li>
        <li>Communicate with your lender or broker to ensure finance is ready for settlement</li>
        <li>Attend to exchange of contracts</li>
        <li>Advise in relation to mortgage documents</li>
        <li>Preparation of transfer documents</li>
        <li>Liaising with your lender and the agent</li>
        <li>Calculation of settlement adjustments</li>
        <li>Preparing and attending settlement</li>
        <li>Communicating and keeping you updated on the progress of your matter</li>
      </ul>
    </section>
  </main>
</body>
</html>
```